Astrology Reading Website to attract clients

I need a website for my astrology practice. My business name is Willow Tide Astrology. I will need a page the following pages: About, Readings, Booking, Contact, and Blog. I will need full figma or figma-like mockups of pages along with assets. I will need both desktop and mobile designs.
I like creams, dark blues and greens. I am fine with planets or other astrology symbolism.

Target Market(s)

new age, spiritual

Industry/Entity Type

Holistic, spiritual

Number of Pages Required

3 page

Colors
0054AA
0677BA
7BADD7
CADEEF
E8F1F8

Requirements
Nice to have
• calm and grounded backgrounds

```html
<!DOCTYPE html>
<html lang="en">
<head>
<meta charset="utf-8">
<title>Willow Tide Astrology</title>
<link href="https://fonts.googleapis.com/css2?family=Lato:wght@400;700&display=swap" rel="stylesheet">
<style>
:root{
  --navy:#0c3872;
  --navy-deep:#082a58;
  --green:#3cb54a;
  --ink:#222222;
  --body:#4a4a4a;
  --field:#ececec;
  --footer:#111111;
  --white:#ffffff;
}
*{box-sizing:border-box;margin:0;padding:0}
html,body{width:1200px;height:3476px;overflow:hidden;background:var(--white)}
body{font-family:'Lato',sans-serif;color:var(--ink);position:relative}
.abs{position:absolute}
.btn{position:absolute;background:var(--green);color:var(--white);font-weight:700;font-size:15px;display:flex;align-items:center;justify-content:center;border-radius:3px}
.accent{color:var(--navy)}
.green{color:var(--green)}
h2.section-title{font-size:41px;font-weight:700;letter-spacing:-.3px}

/* header */
.brand{left:111px;top:14px;width:270px;font-size:43px;line-height:48px;text-align:center;font-weight:400;color:#2a2a2a}
.nav{left:491px;top:45px;display:flex;gap:0}
.nav a{display:flex;align-items:center;justify-content:center;height:37px;font-size:15px;color:#555;text-decoration:none}
.nav a.active{background:var(--navy);color:var(--white);width:70px;border-radius:3px;font-weight:700}

/* hero */
.hero{left:0;top:128px;width:1200px;height:601px;border-radius:0 0 60px 60px;overflow:hidden;
  background:radial-gradient(circle at 820px 305px,#ffe7a8 0,#f2a43b 40px,#b8611c 130px,#5a2c12 230px,rgba(20,15,20,0) 340px),
  radial-gradient(ellipse at 1000px 50px,#2a3550 0,rgba(0,0,0,0) 300px),#07070d}
.hero-title{left:111px;top:250px;font-size:78px;line-height:81px;color:var(--white);font-weight:700;letter-spacing:-.5px}
.hero-text{left:112px;top:440px;width:410px;font-size:18px;line-height:26px;color:var(--white)}

/* about */
.about-img{left:111px;top:814px;width:437px;height:520px;border-radius:16px;
  background:radial-gradient(circle at 230px 210px,#fff3d6 0,#f2a85a 60px,#9b4e6e 170px,#3a2a5a 260px,#151628 360px)}
.about-title{left:632px;top:806px}
.about-text{left:631px;top:882px;width:460px;font-size:14.6px;line-height:25px;color:var(--body)}
.about-text p+p{margin-top:25px}

/* readings */
.readings{left:45px;top:1420px;width:1112px;height:392px;border-radius:18px;
  background:radial-gradient(ellipse at 550px 120px,#1d4f8c 0,#0f3d78 300px,#0a3068 600px)}
.readings h2{position:absolute;left:0;width:100%;top:66px;text-align:center;color:var(--white)}
.readings p{position:absolute;left:156px;width:800px;top:131px;text-align:center;color:var(--white);font-size:15px;line-height:23.2px}

/* booking */
.book-title{left:112px;top:1889px}
.book-sub{left:111px;top:1951px;font-size:15.5px;font-weight:700;color:var(--green)}
.book-text{left:111px;top:1985px;width:490px;font-size:14px;line-height:20.5px;color:var(--body)}
.field{position:absolute;left:111px;width:450px;height:42px;background:var(--field);font-size:13.5px;color:#555;padding:13px 17px}
.book-img{left:652px;top:1898px;width:436px;height:518px;border-radius:16px;
  background:radial-gradient(circle at 225px 255px,#fff6d8 0,#f5b04a 50px,#c26a20 150px,#5c3a24 260px,#3c3430 380px)}

/* testimonials */
.clients-title{left:0;width:1200px;top:2492px;text-align:center}
.card{position:absolute;top:2580px;width:310px;height:360px;background:var(--white);box-shadow:0 0 10px rgba(0,0,0,.12);text-align:center}
.avatar{width:116px;height:116px;border-radius:50%;margin:40px auto 0;background:linear-gradient(#c9c9c9,#9a9a9a)}
.card h3{margin-top:16px;font-size:21px;font-weight:400;color:var(--green)}
.card .role{font-size:13.5px;color:#666;margin-top:6px}
.card p{font-size:13px;line-height:20px;color:#555;margin:10px 20px 0}
.card.current::after{content:"";position:absolute;left:0;bottom:-2px;width:100%;height:5px;background:var(--navy)}
.dots{left:565px;top:2966px;display:flex;gap:3px}
.dots span{width:8px;height:7px;background:#bcbcbc}
.dots span.on{width:36px;background:var(--navy)}

/* footer */
.footer{left:0;top:3064px;width:1200px;height:412px;background:var(--footer);color:var(--white)}
.footer h4{position:absolute;top:78px;font-size:21px;font-weight:700}
.footer .col-text{position:absolute;font-size:15px;line-height:26px}
.footer ul{position:absolute;top:124px;list-style:none;font-size:15px}
.footer li{height:38.7px}
.socials{position:absolute;left:113px;top:256px;display:flex;gap:19px;align-items:center}
.socials span{width:28px;height:28px;border:2px solid var(--white);border-radius:5px}
.socials span.first{width:38px;height:38px;background:var(--green);border:none}
.contact-row{position:absolute;left:634px;display:flex;gap:20px;font-size:15px;line-height:26px}
.contact-row svg{flex:none;margin-top:4px}
.rule{position:absolute;left:111px;top:368px;width:977px;height:1px;background:#333}
.copy{position:absolute;left:0;width:1200px;top:384px;text-align:center;font-size:13px}
</style>
</head>
<body>

<header>
  <div class="abs brand">Willow Tide<br>Astrology</div>
  <nav class="abs nav">
    <a class="active" href="#">Home</a>
    <a href="#" style="margin-left:30px;width:65px">About</a>
    <a href="#" style="margin-left:30px;width:74px">Readings</a>
    <a href="#" style="margin-left:30px;width:67px">Booking</a>
    <a href="#" style="margin-left:30px;width:55px">Blog</a>
    <a href="#" style="margin-left:30px;width:65px">Contact</a>
  </nav>
</header>

<section class="abs hero" role="img" aria-label="Starry night sky with a glowing golden zodiac wheel"></section>
<h1 class="abs hero-title">Willow Tide<br>Astrology</h1>
<p class="abs hero-text">Lorem ipsum dolor sit amet, consectetur adipiscing elit, sed do eiusmod tempor incididunt ut labore et dolore magna aliqua.</p>
<a class="btn" style="left:111px;top:553px;width:189px;height:42px">Book Your Reading</a>

<div class="abs about-img" role="img" aria-label="Silhouette meditating before a colourful galaxy"></div>
<h2 class="abs section-title about-title">About <span class="accent">Us</span></h2>
<div class="abs about-text">
  <p>Lorem ipsum dolor sit amet, consectetur adipiscing elit, sed do eiusmod tempor incididunt ut labore et dolore magna aliqua. Ut enim ad minim veniam, quis nostrud exercitation ullamco laboris nisi ut aliquip ex ea commodo consequat. Duis aute irure dolor in reprehenderit in voluptate velit esse cillum dolore eu fugiat nulla pariatur.</p>
  <p>Sed ut perspiciatis unde omnis iste natus error sit voluptatem accusantium doloremque laudantium, totam rem aperiam, eaque ipsa quae ab illo inventore veritatis et quasi architecto beatae vitae dicta sunt explicabo. Nemo enim ipsam voluptatem quia voluptas sit aspernatur aut odit aut fugit, sed quia consequuntur magni dolores eos qui ratione voluptatem sequi nesciunt. Neque porro quisquam est, qui dolorem ipsum quia dolor sit amet, consectetur, adipisci velit, dolore magnam aliquam quaerat voluptatem.</p>
</div>
<a class="btn" style="left:632px;top:1291px;width:137px;height:43px">Read More</a>

<section class="abs readings">
  <h2 class="section-title">Readings</h2>
  <p>Lorem ipsum dolor sit amet, consectetur adipiscing elit, sed do eiusmod tempor incididunt ut labore et dolore magna aliqua. Ut enim ad minim veniam, quis nostrud exercitation ullamco laboris nisi ut aliquip ex ea commodo consequat. Duis aute irure dolor in reprehenderit in voluptate velit esse cillum dolore eu fugiat nulla pariatur. Sed ut perspiciatis unde omnis iste natus error sit voluptatem accusantium doloremque laudantium, totam rem aperiam, eaque ipsa quae ab illo inventore veritatis et quasi architecto beatae vitae dicta sunt explicabo.</p>
  <a class="btn" style="left:487px;top:274px;width:137px;height:43px">Read More</a>
</section>

<h2 class="abs section-title book-title">Book Your <span class="accent">Cosmic Session</span></h2>
<div class="abs book-sub">Connect with the Stars and Unlock Your Potential</div>
<p class="abs book-text">Lorem ipsum dolor sit amet, consectetur adipiscing elit, sed do minim veniam, quis nostrud exercitation ullamco laboris nisi ut aliquipeiusmod tempor incididunt ut labore et dolore magna aliqua.</p>
<form>
  <div class="field" style="top:2076px">Name</div>
  <div class="field" style="top:2131px">Phone</div>
  <div class="field" style="top:2187px">Email</div>
  <div class="field" style="top:2242px;height:101px">Message</div>
  <div class="btn" style="left:111px;top:2374px;width:139px;height:42px">Submit</div>
</form>
<div class="abs book-img" role="img" aria-label="Open book glowing beneath a golden zodiac wheel"></div>

<h2 class="abs section-title clients-title">What Our <span class="accent">Clients Say</span></h2>
<div class="card" style="left:111px"><div class="avatar" role="img" aria-label="Client portrait"></div><h3>M. Harlow</h3><div class="role">Clients 1</div><p>Duis aute irure dolor in reprehenderit in vo luptate velit esse cillum dolore eu fugiat nulla pariatur. Excepteur sint occaecat cupidatat non proident, sunt in culpa qui officia dese runt mollit anim id est laborum.</p></div>
<div class="card current" style="left:444px"><div class="avatar" role="img" aria-label="Client portrait"></div><h3>T. Penrose</h3><div class="role">Clients 2</div><p>Duis aute irure dolor in reprehenderit in vo luptate velit esse cillum dolore eu fugiat nulla pariatur. Excepteur sint occaecat cupidatat non proident, sunt in culpa qui officia dese runt mollit anim id est laborum.</p></div>
<div class="card" style="left:778px"><div class="avatar" role="img" aria-label="Client portrait"></div><h3>S. Ellery</h3><div class="role">Clients 3</div><p>Duis aute irure dolor in reprehenderit in vo luptate velit esse cillum dolore eu fugiat nulla pariatur. Excepteur sint occaecat cupidatat non proident, sunt in culpa qui officia dese runt mollit anim id est laborum.</p></div>
<div class="abs dots"><span class="on"></span><span></span><span></span><span></span></div>

<footer class="abs footer">
  <h4 style="left:113px">About <span class="green">Us</span></h4>
  <p class="col-text" style="left:113px;top:124px;width:240px">Lorem ipsum dolor sit amet, consectetur adipiscing elit, sed do eiusmod tempor incididunt ut labore et dolore magna aliqua.</p>
  <div class="socials"><span class="first"></span><span></span><span></span><span></span></div>

  <h4 style="left:429px">Quick <span class="green">Links</span></h4>
  <ul style="left:429px"><li>Home</li><li>About</li><li>Readings</li><li>Booking</li><li>Blog</li></ul>

  <h4 style="left:634px">Contact <span class="green">Us</span></h4>
  <div class="contact-row" style="top:124px">
    <svg width="19" height="22" viewBox="0 0 19 22" fill="none" stroke="#fff" stroke-width="1.6"><path d="M9.5 21s-7.5-7-7.5-12a7.5 7.5 0 0 1 15 0c0 5-7.5 12-7.5 12z"/><circle cx="9.5" cy="9" r="2.6"/></svg>
    <span>48, Willow Tide Lane<br>Lorem ipsum<br>dolor sit amet Na 204517</span>
  </div>
  <div class="contact-row" style="top:226px">
    <svg width="19" height="19" viewBox="0 0 24 24" fill="none" stroke="#fff" stroke-width="1.6"><path d="M22 16.9v3a2 2 0 0 1-2.2 2 19.8 19.8 0 0 1-8.6-3.1 19.5 19.5 0 0 1-6-6A19.8 19.8 0 0 1 2.1 4.2 2 2 0 0 1 4.1 2h3a2 2 0 0 1 2 1.7c.1 1 .4 1.9.7 2.8a2 2 0 0 1-.5 2.1L8 9.9a16 16 0 0 0 6 6l1.3-1.3a2 2 0 0 1 2.1-.4c.9.3 1.8.6 2.8.7a2 2 0 0 1 1.7 2z"/></svg>
    <span>+ 1 555 014 2290</span>
  </div>
  <div class="contact-row" style="top:278px">
    <svg width="19" height="19" viewBox="0 0 24 24" fill="none" stroke="#fff" stroke-width="1.6"><rect x="2" y="4" width="20" height="16" rx="2"/><path d="M2 6l10 7 10-7"/></svg>
    <span>info@willowtideastrology.com</span>
  </div>

  <h4 style="left:979px">Other <span class="green">Links</span></h4>
  <ul style="left:979px"><li>Contact</li><li>FAQs</li><li>SItemap</li><li>Resources</li><li>Privacy Policy</li></ul>

  <div class="rule"></div>
  <div class="copy">Copyright © 2024 Willow Tide Astrology. All Rights Reserved.</div>
</footer>

</body>
</html>
```